Innovative Freezer Label Design

Create a versatile and innovative freezer label design with universal appeal, suitable for different functionalities. The design should cater to a diverse audience, including those who freeze meals for meal prepping, batch cooking, and the restaurant industry. Our vision is a visually striking and distinctive design that embodies simplicity.

Example "our current labels feature essential details like "Contents" and "Date." We recognize these as crucial points of information. Currently, the challenge lies in creating various labels for different marketplaces, considering language barriers. A proposed solution involves the integration of universal icons to replace specific words, promoting practicality for international sales."

Kindly note that design concepts should not be restricted to our current product, brand guideline, logo, or the provided example.

Our goal is not only product differentiation but also increased sales through a blend of functionality and aesthetics.

The following are examples of freezer labels designs. Kindly do not restrict your designs to the examples. The designs must be universal (for language barrier purposes)

Examples:
https://www.snaprovel.co.uk/pin/5820174630298837415/
https://www.snaprovel.co.uk/pin/5820174630298837419/
https://www.snaprovel.co.uk/pin/5820174630298837408/
https://www.snaprovel.co.uk/pin/5820174630298837322/
https://www.snaprovel.co.uk/pin/5820174630298898764/

Please reach out if you have any questions.

Thank you

```html
<!DOCTYPE html>
<html lang="en">
<head>
<meta charset="utf-8">
<title>Velto FreshKeep — Freezer Labels</title>
<link href="https://fonts.googleapis.com/css2?family=EB+Garamond:wght@600&family=Montserrat:wght@500&display=swap" rel="stylesheet">
<style>
  :root {
    --sage: #93aea3;
    --slate: #374e5b;
    --paper: #ffffff;
  }
  html, body {
    margin: 0;
    width: 1200px;
    height: 1200px;
    overflow: hidden;
    background: var(--paper);
  }
  .sheet { display: block; width: 1200px; height: 1200px; }
  .theme-sage { color: var(--sage); }
  .theme-slate { color: var(--slate); }
  .frame { fill: var(--paper); stroke: currentColor; stroke-width: 2.5; }
  .band, .header, .badge { fill: currentColor; }
  .divider { stroke: currentColor; stroke-width: 2.5; }
  .slash { stroke: currentColor; stroke-width: 2.5; stroke-linecap: round; }
  .brand { font-family: "EB Garamond", Georgia, serif; font-weight: 600; fill: currentColor; text-anchor: middle; }
  .brand-name { font-size: 40px; letter-spacing: 3px; }
  .brand-line { font-size: 16px; letter-spacing: 1.5px; }
  .on-fill .brand { fill: var(--paper); }
  .field-title { font-family: "Montserrat", Arial, sans-serif; font-weight: 500; font-size: 17px; fill: var(--paper); }
  .icon { color: var(--paper); }
</style>
</head>
<body>
<svg class="sheet" viewBox="0 0 1160 1160" xmlns="http://www.w3.org/2000/svg" role="group" aria-label="Six freezer label variants">
  <defs>
    <symbol id="icon-note" viewBox="0 0 30 30">
      <g fill="none" stroke="currentColor" stroke-width="1.8" stroke-linecap="round" stroke-linejoin="round">
        <path d="M19 26H5a2.5 2.5 0 0 1-2.5-2.5v-19A2.5 2.5 0 0 1 5 2h14a2.5 2.5 0 0 1 2.5 2.5V12"/>
        <path d="M7 8h10M7 12.5h10M7 17h6M7 21.5h4"/>
        <path d="M24.5 13.5l3 3-8 8-3.8.8.8-3.8z"/>
      </g>
    </symbol>
    <symbol id="icon-calendar" viewBox="0 0 30 30">
      <g fill="none" stroke="currentColor" stroke-width="1.8" stroke-linecap="round" stroke-linejoin="round">
        <rect x="2" y="5" width="26" height="23" rx="2.5"/>
        <path d="M2 10.5h26M8 2.5v5M15 2.5v5M22 2.5v5"/>
      </g>
      <g fill="currentColor">
        <rect x="7" y="14" width="3" height="2.6"/><rect x="11.5" y="14" width="3" height="2.6"/><rect x="16" y="14" width="3" height="2.6"/><rect x="20.5" y="14" width="3" height="2.6"/>
        <rect x="7" y="18.3" width="3" height="2.6"/><rect x="11.5" y="18.3" width="3" height="2.6"/><rect x="16" y="18.3" width="3" height="2.6"/><rect x="20.5" y="18.3" width="3" height="2.6"/>
        <rect x="7" y="22.6" width="3" height="2.6"/><rect x="11.5" y="22.6" width="3" height="2.6"/><rect x="16" y="22.6" width="3" height="2.6"/><rect x="20.5" y="22.6" width="3" height="2.6"/>
      </g>
    </symbol>

    <g id="label-banded-words">
      <rect class="frame" x="180" y="115" width="360" height="257"/>
      <text class="brand brand-name" x="360" y="158">VELTO</text>
      <text class="brand brand-line" x="360" y="176">FreshKeep</text>
      <rect class="band" x="181" y="186" width="358" height="36"/>
      <use class="icon" href="#icon-note" x="264" y="189" width="30" height="30"/>
      <text class="field-title" x="307" y="211">CONTENTS:</text>
      <rect class="band" x="181" y="286" width="358" height="37"/>
      <use class="icon" href="#icon-calendar" x="265" y="290" width="30" height="30"/>
      <text class="field-title" x="334" y="312">DATE:</text>
      <line class="slash" x1="327" y1="338" x2="321" y2="358"/>
      <line class="slash" x1="400" y1="338" x2="394" y2="358"/>
    </g>

    <g id="label-badges">
      <rect class="frame" x="180" y="451" width="360" height="240" rx="14"/>
      <path class="header" d="M180 465a14 14 0 0 1 14-14h332a14 14 0 0 1 14 14v52H180z"/>
      <g class="on-fill">
        <text class="brand brand-name" x="360" y="492">VELTO</text>
        <text class="brand brand-line" x="360" y="510">FreshKeep</text>
      </g>
      <line class="divider" x1="181" y1="615" x2="539" y2="615"/>
      <circle class="badge" cx="230" cy="560" r="26"/>
      <use class="icon" href="#icon-note" x="217" y="547" width="26" height="26"/>
      <circle class="badge" cx="230" cy="656" r="26"/>
      <use class="icon" href="#icon-calendar" x="217" y="643" width="26" height="26"/>
      <line class="slash" x1="345" y1="646" x2="339" y2="666"/>
      <line class="slash" x1="443" y1="646" x2="437" y2="666"/>
    </g>

    <g id="label-banded-icons">
      <rect class="frame" x="180" y="781" width="360" height="258" rx="14"/>
      <text class="brand brand-name" x="360" y="824">VELTO</text>
      <text class="brand brand-line" x="360" y="842">FreshKeep</text>
      <rect class="band" x="181" y="853" width="358" height="36"/>
      <use class="icon" href="#icon-note" x="347" y="856" width="30" height="30"/>
      <rect class="band" x="181" y="953" width="358" height="37"/>
      <use class="icon" href="#icon-calendar" x="348" y="957" width="30" height="30"/>
      <line class="slash" x1="327" y1="1005" x2="321" y2="1025"/>
      <line class="slash" x1="400" y1="1005" x2="394" y2="1025"/>
    </g>
  </defs>

  <g class="theme-sage">
    <use href="#label-banded-words"/>
    <use href="#label-badges"/>
    <use href="#label-banded-icons"/>
  </g>
  <g class="theme-slate" transform="translate(443,0)">
    <use href="#label-banded-words"/>
    <use href="#label-badges"/>
    <use href="#label-banded-icons"/>
  </g>
</svg>
</body>
</html>
```